Marigold Shore Realty business card design

Looking for an upscale and clean business card design and updated logo. I sell to a very high-end south Florida real estate market.
Target Market(s)
High-end real estate in south Florida real estate market
Industry/Entity Type
Real Estate Agent
Contact Information for Business Card
Marigold Shore Realty, Inc
738 West Penrick Ave, Suite 400/500, Fort Lauderdale, FL 33315
Tim Harlow - Broker/Owner
954-327-8846 Direct
timshomes@quillmail.net
Website: StayPenrickAv.net
Font styles to use
Other font styles liked:
- Copperplate Gothic, Georgia, etc.
Requirements
Must have
- My photo, company name, my name and title, all info stated in Details above
Nice to have
- Luxury home design element, waterfront

```html
<!DOCTYPE html>
<html lang="en">
<head>
<meta charset="utf-8">
<title>Marigold Shore Realty – Business Card</title>
<link rel="stylesheet" href="https://fonts.googleapis.com/css2?family=EB+Garamond:wght@400&family=Michroma&family=Open+Sans:wght@400;600&display=swap">
<style>
  :root {
    --backdrop: #1c1c1c;
    --paper: #ffffff;
    --ink: #111111;
    --sun: #f4c63d;
    --muted: #333333;
  }
  * { margin: 0; padding: 0; box-sizing: border-box; }
  html, body { width: 1200px; height: 1015px; overflow: hidden; }
  body {
    background: var(--backdrop);
    font-family: "Open Sans", sans-serif;
    position: relative;
  }
  .card {
    position: absolute;
    left: 220px;
    width: 760px;
    height: 434px;
    background: var(--paper);
    overflow: hidden;
    box-shadow: 0 10px 30px rgba(0,0,0,.5);
  }
  .card--front { top: 50px; }
  .card--back { top: 531px; }

  .brand {
    display: flex;
    align-items: center;
    gap: 14px;
    font-family: "EB Garamond", serif;
    font-weight: 400;
    color: var(--ink);
    white-space: nowrap;
  }
  .brand__dot {
    border-radius: 50%;
    background: var(--sun);
    flex: none;
  }
  .card--front .brand {
    position: absolute;
    left: 50%; top: 50%;
    transform: translate(-50%, -50%);
    font-size: 40px;
  }
  .card--front .brand__dot { width: 34px; height: 34px; }

  .card--back .brand {
    position: absolute;
    right: 40px; top: 44px;
    font-size: 24px;
    gap: 10px;
    z-index: 1;
  }
  .card--back .brand__dot { width: 22px; height: 22px; }

  .wave { position: absolute; inset: 0; width: 100%; height: 100%; }

  .person { position: absolute; left: 42px; top: 96px; z-index: 1; }
  .person__name {
    font-family: "Michroma", sans-serif;
    color: var(--sun);
    font-size: 19px;
    letter-spacing: 4px;
  }
  .person__title {
    font-size: 12px;
    color: var(--muted);
    margin-top: 2px;
  }
  .contacts { list-style: none; margin-top: 18px; }
  .contacts li {
    display: flex;
    align-items: center;
    gap: 12px;
    font-size: 16px;
    color: var(--ink);
    line-height: 27px;
  }
  .contacts svg { width: 16px; height: 16px; flex: none; fill: var(--sun); }

  .website {
    position: absolute;
    right: 36px; top: 302px;
    color: var(--paper);
    font-size: 15px;
    letter-spacing: 4px;
    z-index: 1;
  }
  .address {
    position: absolute;
    left: 132px; bottom: 30px;
    color: var(--paper);
    font-size: 16px;
    font-style: normal;
    line-height: 22px;
    z-index: 1;
  }
</style>
</head>
<body>

<section class="card card--front" aria-label="Card front">
  <div class="brand"><span class="brand__dot"></span>Marigold Shore Realty, Inc</div>
</section>

<section class="card card--back" aria-label="Card back">
  <svg class="wave" viewBox="0 0 760 434" aria-hidden="true">
    <path d="M22,434 C72,318 180,285 380,269 C565,253 692,200 760,80 L760,94 C692,212 560,262 380,279 C180,293 78,326 30,434 Z" fill="var(--sun)"/>
    <path d="M38,434 C88,332 184,302 380,288 C562,273 694,224 760,108 L760,434 Z" fill="var(--ink)"/>
  </svg>

  <div class="brand"><span class="brand__dot"></span>Marigold Shore Realty, Inc</div>

  <div class="person">
    <p class="person__name">DALE WHITCOMB</p>
    <p class="person__title">CEO/Managing Director</p>
    <ul class="contacts">
      <li>
        <svg viewBox="0 0 24 24"><path d="M6.6 10.8a15 15 0 0 0 6.6 6.6l2.2-2.2a1 1 0 0 1 1-.25 11.4 11.4 0 0 0 3.6.57 1 1 0 0 1 1 1V20a1 1 0 0 1-1 1A17 17 0 0 1 3 4a1 1 0 0 1 1-1h3.5a1 1 0 0 1 1 1c0 1.25.2 2.45.57 3.57a1 1 0 0 1-.25 1z"/></svg>
        214-555-0143
      </li>
      <li>
        <svg viewBox="0 0 24 24"><path d="M7 3h10v5H7zM4 9h16a2 2 0 0 1 2 2v6h-4v4H6v-4H2v-6a2 2 0 0 1 2-2zm4 8v2h8v-4H8z"/></svg>
        214-555-0143
      </li>
      <li>
        <svg viewBox="0 0 24 24"><path d="M2 5h20v14H2zm2 2v.5l8 5 8-5V7z"/></svg>
        dalewhitcomb@postbay.net
      </li>
    </ul>
  </div>

  <p class="website">www.harborlanes.com</p>

  <address class="address">
    415 Corlett Avenue NW<br>
    Suite 300, Grand Harbor<br>
    MI 49580
  </address>
</section>

</body>
</html>
```